Modern design for a Septic Tank maintenance company

Task Description
- The design should be based around the attached HPID (home page information design) called Tane Drain Septic Services HPID. The table boxes are just for approximate placement of information – you DON'T have to make it look exactly like this.
- Information only is in orange text. Copy to go on the design in black text. Some instructions are in the HPID. Please be creative! You don’t have to use the exact images provided if you have a better idea.

- The design needs to be clean and spacious. Please use the colours from the logos in the website design. LOTS of white too. Don't need to use all the images attached some are customer supplied and might only be good for the smaller images.

I've attached home page gallery example photo called Piha beach. You can use this or something similar - be creative please!

Width of content will be 1100 pixels when implemented as a web page. Header height (without nav bar) 150-160 pixels.

The winning PSD file will have to be provided as follows…
1. Canvas size of 2000px x 2000px - 72ppi in Adobe Photoshop (CS5 compatible)
2. Width of content section is 1100px wide - centered in the canvas
3. Any button rollovers/hovers in the PSD as hidden layers.
4. All fonts used must be Google fonts (except for the fonts in the header at the top of the page).
5. You will need to supply the chosen home page plus one example page (example page as a style guide for how all other pages will look). Example page is only the header and navigational bar at the top, an empty sector in the middle with a column (180 px wide) which can be left or right aligned which means the main sector is 920 pixels wide, and then the footer at the bottom of the page.

```html
<!DOCTYPE html>
<html lang="en">
<head>
<meta charset="utf-8">
<title>Tane Drain Septic Services</title>
<link rel="stylesheet" href="https://fonts.googleapis.com/css2?family=Roboto:wght@300;400;500&display=swap">
<style>
:root{
  --teal:#1cc9a6;
  --ink:#222;
  --grey-text:#666;
  --tagline:#555;
  --nav-top:#4a4a4a;
  --nav-bottom:#2b2b2b;
  --hero-a:#8fa9b3;
  --hero-b:#6f7d68;
  --panel:#444;
  --field:#f1f1f1;
  --card-border:#dcdcdc;
  --footer-bg:#fafafa;
  --base:#111;
}
*{margin:0;padding:0;box-sizing:border-box}
html,body{width:905px;height:1200px;overflow:hidden;background:#fff}
body{position:relative;font-family:'Roboto',sans-serif;color:var(--ink)}
.abs{position:absolute}
.brand{left:126px;top:38px;display:flex;align-items:center;gap:9px;width:240px}
.brand-dot{width:22px;height:22px;border-radius:50%;background:var(--teal);flex:none}
.brand-name{font-size:15px;font-weight:500;color:var(--ink);line-height:1;white-space:nowrap}
.tagline{left:380px;top:32px;width:192px;font-size:9.5px;line-height:15px;color:var(--tagline);text-align:center;font-weight:400}
.header-contact{right:130px;top:32px;text-align:right;font-size:9px;line-height:13px;color:var(--ink)}
.header-contact .phone{display:inline-flex;align-items:center;gap:6px}
.nav{left:126px;top:92px;width:651px;height:46px;display:flex;background:linear-gradient(var(--nav-top),var(--nav-bottom))}
.nav a{display:flex;align-items:center;justify-content:center;color:#fff;font-size:11px;text-decoration:none;border-right:1px solid #555;font-weight:400}
.nav a:last-child{border-right:0}
.nav a.active{background:var(--teal)}
.hero{left:126px;top:139px;width:651px;height:335px;background:linear-gradient(135deg,var(--hero-a),var(--hero-b))}
.hero-caption{left:126px;top:282px;width:489px;height:95px;background:rgba(40,50,50,.72);color:#fff;padding:14px 0 0 19px}
.hero-caption h2{font-size:14.5px;font-weight:400;letter-spacing:-.1px}
.hero-caption p{width:420px;font-size:14.5px;font-weight:500;line-height:22px;margin:6px 0 0 3px}
.dots{left:427px;top:456px;display:flex;gap:6px}
.dots span{width:9px;height:9px;border-radius:50%;background:#fff}
.dots span.on{background:var(--teal)}
.card{top:486px;height:282px;border:1px solid var(--card-border);box-shadow:inset 0 0 12px rgba(0,0,0,.05);background:#fff}
.card h3{position:absolute;left:15px;top:9px;width:185px;font-size:10.5px;font-weight:400;line-height:15px;color:var(--ink)}
.card .photo{position:absolute;left:13px;top:46px;width:184px;height:98px}
.card p{position:absolute;left:17px;top:151px;width:176px;height:66px;overflow:hidden;font-size:9px;line-height:16.3px;color:var(--grey-text);text-align:justify;font-weight:300}
.card .more{position:absolute;left:61px;top:234px;width:87px;height:26px;background:var(--teal);color:#fff;font-size:11px;display:flex;align-items:center;justify-content:center}
.enquiry{left:125px;top:781px;width:651px;height:168px;background:var(--panel)}
.enquiry h2{position:absolute;left:27px;top:30px;font-size:22px;font-weight:400;color:#fff}
.enquiry .lead{position:absolute;left:27px;top:68px;width:210px;font-size:13px;line-height:22px;color:#fff;font-weight:300}
.field{position:absolute;background:var(--field);font-size:8px;color:var(--ink);padding:0 6px;display:flex;align-items:center}
.field.area{align-items:flex-start;padding-top:8px}
.send{position:absolute;left:519px;top:122px;width:87px;height:27px;background:var(--teal);color:#fff;font-size:11px;display:flex;align-items:center;justify-content:center}
.footer{left:0;top:969px;width:905px;height:169px;background:var(--footer-bg);border-top:1px solid #ddd}
.footer h4{position:absolute;color:var(--teal);font-weight:400;font-size:10px}
.footer h4.big{font-size:12px}
.footer ul{position:absolute;list-style:none;font-size:7.5px;line-height:14.4px;color:#444}
.footer p{position:absolute;font-size:7.5px;line-height:14.4px;color:#444;text-align:justify}
.base{left:0;top:1138px;width:905px;height:62px;background:var(--base)}
.base .copy{position:absolute;left:134px;top:25px;font-size:9px;color:#ddd}
.social{position:absolute;left:670px;top:19px;display:flex;gap:6px}
.social span{width:22px;height:22px;border-radius:50%;background:#fff}
</style>
</head>
<body>
<header>
  <div class="abs brand"><span class="brand-dot"></span><span class="brand-name">Tane Drain Septic Services</span></div>
  <p class="abs tagline">Our Septic tank maintenance services will help your septic system perform at optimum efficiency</p>
  <div class="abs header-contact">
    <div>For Septic Tank servicing, installation</div>
    <div>and parts Auckland Wide</div>
    <div class="phone"><svg width="14" height="14" viewBox="0 0 14 14"><circle cx="7" cy="7" r="6.2" fill="none" stroke="#1cc9a6" stroke-width="1.2"/><path d="M4.6 3.8c.4-.3.8-.2 1 .2l.6 1.1c.2.3.1.6-.2.8l-.4.3c.4.9 1 1.5 1.9 1.9l.3-.4c.2-.3.5-.4.8-.2l1.1.6c.4.2.5.6.2 1-.6.9-1.6 1-2.6.5-1.5-.7-2.6-1.8-3.2-3.2-.5-1-.4-2 .5-2.6z" fill="#1cc9a6"/></svg>09 555 0142 , 021 555 0187</div>
  </div>
  <nav class="abs nav">
    <a class="active" style="width:65px">Home</a>
    <a style="width:57px">About</a>
    <a style="width:166px">Deciphering Your Septic tank</a>
    <a style="width:144px">Servicing &amp; Maintenance</a>
    <a style="width:56px">Parts</a>
    <a style="width:84px">Free Quote</a>
    <a style="width:79px">Contact</a>
  </nav>
</header>

<section>
  <div class="abs hero" role="img" aria-label="Gallery photo of a coastal beach with a rocky headland"></div>
  <div class="abs hero-caption">
    <h2>WANT TO LEARN MORE ABOUT HOW YOUR SEPTIC TANK WORKS?</h2>
    <p>Tane Drain Septic Services are Auckland’s best septic tank experts and will tell you everything there is to know..</p>
  </div>
  <div class="abs dots"><span class="on"></span><span></span><span></span><span></span></div>
</section>

<section>
  <article class="abs card" style="left:126px;width:210px">
    <h3>Looking for septic tanks parts in Auckland asap?</h3>
    <div class="photo" role="img" aria-label="Photo of a septic tank lid in a grassy yard" style="background:linear-gradient(#6b5a45,#4f6b2e)"></div>
    <p>If you need replacement parts for septic tanks, call us today! Tane Drain Septic Services will either have or can source the part you need fast and offer septic tank</p>
    <div class="more">MORE INFO</div>
  </article>
  <article class="abs card" style="left:345px;width:210px">
    <h3>Want to know how to take care of your septic tank?</h3>
    <div class="photo" role="img" aria-label="Photo of a septic drainage field with pipes" style="background:linear-gradient(#8a9a6a,#3f6a2c)"></div>
    <p>Most people when they buy a new property with a septic tank don’t understand how their system works, or even what system they have! Tane Drain Septic Services will</p>
    <div class="more">MORE INFO</div>
  </article>
  <article class="abs card" style="left:566px;width:211px">
    <h3>When was the last time you serviced your septic tank?</h3>
    <div class="photo" role="img" aria-label="Photo of a cleared section surrounded by bush" style="background:linear-gradient(#5a7a4a,#6e6a4e)"></div>
    <p>Standard septic tanks need to be serviced every 3 - 5 years and as each septic system has its own unique characteristics, such as internal parts and control panels. It can</p>
    <div class="more">MORE INFO</div>
  </article>
</section>

<section class="abs enquiry">
  <h2>MAKE AN ENQUIRY</h2>
  <p class="lead">Fill out the form below and we will contact you within 24hrs</p>
  <div class="field" style="left:239px;top:28px;width:203px;height:25px">Name *</div>
  <div class="field" style="left:239px;top:60px;width:203px;height:24px">Email *</div>
  <div class="field" style="left:239px;top:92px;width:203px;height:24px">Contact phone *</div>
  <div class="field area" style="left:449px;top:28px;width:157px;height:88px">Details</div>
  <div class="send">SEND</div>
</section>

<footer class="abs footer">
  <h4 class="big" style="left:133px;top:25px">CONTACT INFO</h4>
  <ul style="left:134px;top:50px">
    <li>Home</li><li>About</li><li>Deciphering Your Septic tank</li><li>Servicing &amp; Maintenance</li><li>Parts</li><li>Free Quote</li><li>Contact</li>
  </ul>
  <h4 style="left:337px;top:27px">COMPANY GUARANTEE TO YOU...</h4>
  <p style="left:337px;top:50px;width:178px">Tane Drain Septic Services travel throughout the Auckland region. Owner Rhys promises they will go through your system with a fine tooth comb and provide a comprehensive service.</p>
  <p style="left:337px;top:122px;width:178px;text-align:left">Tane Drain Septic Services aim to give clients more than they expect from their septic tank service.</p>
  <h4 style="left:571px;top:27px">NEED YOUR SEPTIC TANK CLEANED?</h4>
  <p style="left:573px;top:54px;width:200px;text-align:left">Talk to the team at Kowhai Tank Cleaning Services!</p>
  <h4 style="left:568px;top:98px">FOR ALL POLYMER FABRICATED PRODUCTS</h4>
  <p style="left:572px;top:117px;width:200px;text-align:left">- Talk to the team at Harbour Poly Works Limited!</p>
</footer>

<div class="abs base">
  <span class="copy">© Copyright 2014 &nbsp; All Rights Reserved</span>
  <div class="social"><span></span><span></span><span></span><span></span></div>
</div>
</body>
</html>
```